Home care agency

Current website QRVCAREPLUS.com. Need to update and reformat to different pages. use my info from my current website

Target Market(s)

adult children

Industry/Entity Type

Home Health

Coding

Coded - Design and coding required

Number of Pages Required

4 page

Font styles to use
Sans Serif

Colors
3276b5
33a6d7
3277b5
85cae6
85acd3

```html
<!DOCTYPE html>
<html lang="en">
<head>
<meta charset="utf-8">
<title>Care Inquiry Form – Harbor Light Home Care</title>
<link rel="stylesheet" href="https://fonts.googleapis.com/css2?family=Arimo:wght@400;700&display=swap">
<style>
:root{
  --blue-deep:#3276b5;
  --blue-footer:#3277b5;
  --blue-bright:#33a6d7;
  --blue-light:#85cae6;
  --backdrop:#9b9a98;
  --band:#f4f4f3;
  --field:#f6f5f3;
  --field-border:#a3a3a3;
  --rule:#bdbdbd;
  --ink:#222;
  --label:#6a6a6a;
  --required:#d0021b;
  --white:#fff;
}
*{box-sizing:border-box;margin:0;padding:0}
html,body{width:1078px;height:1200px;overflow:hidden}
body{background:var(--backdrop);font-family:"Arimo",Arial,sans-serif;position:relative}
.page{position:absolute;left:210px;top:10px;width:732px;height:1312px;background:var(--white);transform:scale(.9);transform-origin:0 0;overflow:hidden}
.abs{position:absolute}

/* top bar */
.topbar{left:0;top:0;width:732px;height:37px;background:var(--blue-bright);color:var(--white);font-size:11px;display:flex;align-items:center}
.topbar .info{position:absolute;left:84px;display:flex;align-items:center;gap:6px}
.topbar svg{display:block}
.topbar .sep{opacity:.8;margin:0 2px}
.social{position:absolute;right:40px;display:flex;gap:7px}
.social span{width:15px;height:15px;border:1.3px solid var(--white);border-radius:50%}

/* nav */
.nav{left:0;top:37px;width:732px;height:58px}
.brand{position:absolute;left:118px;top:16px;display:flex;align-items:center;gap:6px;font-size:11px;color:var(--blue-deep);font-weight:700}
.brand i{width:26px;height:26px;border:1.5px dashed var(--blue-bright);border-radius:50%}
.menu{position:absolute;left:368px;top:25px;font-size:9px;font-weight:700;color:var(--ink);display:flex;gap:0}
.menu a{color:inherit;text-decoration:none;position:absolute;white-space:nowrap}
.cta{position:absolute;left:592px;top:16px;width:134px;height:28px;border-radius:14px;background:var(--blue-deep);color:var(--white);font-size:11.5px;font-weight:700;display:flex;align-items:center;justify-content:center}

/* title band */
.titleband{left:0;top:95px;width:732px;height:59px;background:var(--band);color:var(--ink);display:flex;align-items:center;padding-left:15px;font-size:24px}
.titleband small{font-size:18px;margin-left:6px}

/* form */
.section{font-size:18px;color:var(--ink)}
.rule{height:1px;background:var(--rule)}
.label{font-size:14px;color:var(--label);white-space:nowrap}
.req{color:var(--required);font-size:12px;vertical-align:top;margin-left:3px}
.field{background:var(--field);border:1.5px solid var(--field-border);height:39px;display:flex;align-items:center;justify-content:center;font-size:14px;color:#8a8a8a}
.radio{width:14px;height:14px;border:1.3px solid #777;border-radius:50%}
.submit{background:var(--blue-deep);color:var(--white);font-size:13px;font-weight:700;display:flex;align-items:center;justify-content:center;border:1px solid #2a5f93}

/* footer */
.footer{left:0;top:1147px;width:732px;height:137px;background:var(--blue-footer);color:var(--white)}
.fhead{position:absolute;font-size:12px;font-weight:700;display:flex;align-items:center;gap:5px;white-space:nowrap}
.fhead::after{content:"";width:40px;height:1px;background:var(--white)}
.ftext{position:absolute;font-size:8px;line-height:10.8px}
.download{position:absolute;left:473px;top:85px;width:174px;height:47px;border:2px solid var(--white);border-radius:14px;background:var(--blue-bright);text-align:center;font-weight:700}
.download small{display:block;font-size:9px;margin-top:8px}
.download b{display:block;font-size:13px}
.legal{left:0;top:1284px;width:732px;height:28px;background:var(--blue-bright);color:var(--white);font-size:8.5px;display:flex;align-items:center;justify-content:center}
</style>
</head>
<body>
<main class="page">

  <div class="abs topbar">
    <div class="info">
      <svg width="10" height="13" viewBox="0 0 10 13"><path d="M5 0a5 5 0 0 1 5 5c0 3.5-5 8-5 8S0 8.5 0 5a5 5 0 0 1 5-5z" fill="#fff"/><circle cx="5" cy="5" r="1.8" fill="#33a6d7"/></svg>
      <span>PO Box 48, Seaview, MA 02190</span><span class="sep">|</span>
      <svg width="14" height="14" viewBox="0 0 14 14"><circle cx="7" cy="7" r="6" fill="none" stroke="#fff" stroke-width="2"/><path d="M7 3.5V7H4.5" stroke="#fff" stroke-width="1.5" fill="none"/></svg>
      <span>Mon - Fri 9:00am-5:00pm</span><span class="sep">|</span>
      <svg width="11" height="11" viewBox="0 0 11 11"><path d="M2 0l2 3-1.2 1.2a6 6 0 0 0 4 4L8 7l3 2-1.2 1.8C5 11 0 6 .2 1.2z" fill="#fff"/></svg>
      <span>555-014-2290.</span>
    </div>
    <div class="social"><span></span><span></span><span></span></div>
  </div>

  <header class="abs nav">
    <div class="brand"><i></i>Harbor Light</div>
    <nav class="menu">
      <a style="left:0">HOME</a>
      <a style="left:46px">ABOUT</a>
      <a style="left:93px">SERVICES</a>
      <a style="left:164px">CONTACT</a>
    </nav>
    <div class="cta">CARE INQUIRY FORM</div>
  </header>

  <h1 class="abs titleband" style="font-weight:400">Care Inquiry Form -<small>Contact Information</small></h1>

  <form>
    <div class="abs section" style="left:46px;top:176px">Contact Name<span class="req">*</span></div>
    <div class="abs rule" style="left:46px;top:205px;width:657px"></div>

    <div class="abs label" style="left:50px;top:222px">First Name</div>
    <div class="abs field" style="left:49px;top:242px;width:301px"></div>
    <div class="abs label" style="left:360px;top:222px">Last Name</div>
    <div class="abs field" style="left:359px;top:242px;width:301px"></div>

    <div class="abs label" style="left:49px;top:293px">Contact Phone Number<span class="req">*</span></div>
    <div class="abs field" style="left:50px;top:318px;width:67px">(###)</div>
    <div class="abs field" style="left:126px;top:318px;width:67px">(###)</div>
    <div class="abs field" style="left:205px;top:318px;width:67px">(####)</div>

    <div class="abs label" style="left:362px;top:290px">Contact E-mail Address<span class="req">*</span></div>
    <div class="abs field" style="left:359px;top:310px;width:301px"></div>

    <div class="abs label" style="left:49px;top:372px">Best Way to Reach You<span class="req">*</span></div>
    <div class="abs radio" style="left:49px;top:396px"></div>
    <div class="abs label" style="left:73px;top:395px">By Phone</div>
    <div class="abs radio" style="left:149px;top:396px"></div>
    <div class="abs label" style="left:172px;top:395px">By Email</div>

    <div class="abs section" style="left:51px;top:435px">Client Information</div>
    <div class="abs rule" style="left:51px;top:460px;width:655px"></div>
    <div class="abs section" style="left:51px;top:472px">Client Name<span class="req">*</span></div>

    <div class="abs label" style="left:52px;top:502px">First Name</div>
    <div class="abs field" style="left:52px;top:522px;width:300px"></div>
    <div class="abs label" style="left:362px;top:502px">Last Name</div>
    <div class="abs field" style="left:362px;top:522px;width:300px"></div>

    <div class="abs label" style="left:53px;top:574px">Client Birthday<span class="req">*</span></div>
    <div class="abs field" style="left:54px;top:599px;width:67px">DD</div>
    <div class="abs field" style="left:137px;top:599px;width:67px">MM</div>
    <div class="abs field" style="left:218px;top:599px;width:67px">YYYY</div>

    <div class="abs label" style="left:55px;top:654px">Address Where Care Will be Provided<span class="req">*</span></div>
    <div class="abs label" style="left:55px;top:684px">Address 1</div>
    <div class="abs field" style="left:53px;top:704px;width:300px"></div>
    <div class="abs label" style="left:368px;top:683px">Address 2</div>
    <div class="abs field" style="left:366px;top:703px;width:300px"></div>

    <div class="abs label" style="left:57px;top:751px">City</div>
    <div class="abs field" style="left:53px;top:770px;width:300px"></div>
    <div class="abs label" style="left:368px;top:752px">State / Province</div>
    <div class="abs field" style="left:368px;top:771px;width:300px"></div>

    <div class="abs label" style="left:57px;top:823px">Zip/Postal Code</div>
    <div class="abs field" style="left:55px;top:846px;width:300px"></div>
    <div class="abs label" style="left:374px;top:822px">Select Your Country</div>
    <div class="abs field" style="left:370px;top:846px;width:300px;justify-content:flex-end;padding-right:10px">
      <svg width="14" height="9" viewBox="0 0 14 9"><path d="M0 0h14L7 9z" fill="#777"/></svg>
    </div>

    <div class="abs label" style="left:56px;top:899px">Please use this area to tell us more about the client and/or services that may be of interest to you.<span class="req">*</span></div>
    <div class="abs field" style="left:53px;top:922px;width:620px;height:128px"></div>

    <div class="abs submit" style="left:53px;top:1068px;width:134px;height:39px">Submit Care Inquiry</div>
  </form>

  <footer class="abs footer">
    <div class="fhead" style="left:110px;top:26px">CONTACT US</div>
    <p class="ftext" style="left:110px;top:49px;width:162px">Thank you for considering Harbor Light Home Care for your care needs. Information about your medical conditions, care, and financial situation that you provide to us in writing, via email, on the phone (including information left on voice mails) is held in strictest confidence.</p>

    <div class="fhead" style="left:293px;top:26px">GET IN TOUCH</div>
    <svg class="abs" style="left:293px;top:51px" width="10" height="13" viewBox="0 0 10 13"><path d="M5 0a5 5 0 0 1 5 5c0 3.5-5 8-5 8S0 8.5 0 5a5 5 0 0 1 5-5z" fill="#fff"/><circle cx="5" cy="5" r="1.8" fill="#3277b5"/></svg>
    <p class="ftext" style="left:314px;top:51px;line-height:9.5px">Harbor Light Home Care<br>PO Box 48<br>Seaview, MA 02190</p>
    <svg class="abs" style="left:293px;top:90px" width="11" height="11" viewBox="0 0 11 11"><path d="M2 0l2 3-1.2 1.2a6 6 0 0 0 4 4L8 7l3 2-1.2 1.8C5 11 0 6 .2 1.2z" fill="#fff"/></svg>
    <svg class="abs" style="left:292px;top:116px" width="12" height="9" viewBox="0 0 12 9"><rect width="12" height="9" fill="#fff"/><path d="M0 0l6 5 6-5" stroke="#3277b5" fill="none"/></svg>
    <p class="ftext" style="left:314px;top:117px">info@qrvcareplus.com</p>

    <div class="fhead" style="left:472px;top:23px">CONTACT ONLINE</div>
    <p class="ftext" style="left:473px;top:45px;width:165px">To contact us online, please fill out the care inquiry form above and you will be contacted within 24-48 hours.</p>
    <div class="download"><small>Download</small><b>Employment Application</b></div>
  </footer>

  <div class="abs legal">Harbor Light Home Care © 2019 All Right Reserved</div>
</main>
</body>
</html>
```